Q827 PowerPoint Presentation

As you can see the design of this PowerPoint isn't cohesive. There are a lot of images and words that give it a very jumbled and busy appeal. We want to turn this into a sharp, cohesive and visually appealing presentation without taking away too much of the information. Feel free to use the images to create your own artwork for the PowerPoint.

Please don't hesitate to contact me with any questions.

```html
<!DOCTYPE html>
<html lang="en">
<head>
<meta charset="utf-8">
<title>Q827 – Idea to Reality</title>
<link href="https://fonts.googleapis.com/css2?family=Carlito:wght@400;700&family=PT+Sans:wght@400;700&display=swap" rel="stylesheet">
<style>
  :root {
    --band-top: #e6eef8;
    --band-bottom: #d3e0f1;
    --title-blue: #4f84c9;
    --rule: #a9b4c2;
    --gold: #e0a500;
    --arrow: #f5b800;
    --step-1: #4f7fc0;
    --step-2: #6f98d3;
    --step-3: #93b5e2;
    --ink: #3d4450;
    --footer: #c9ced6;
    --white: #ffffff;
  }
  * { margin: 0; padding: 0; box-sizing: border-box; }
  html, body { width: 1200px; height: 675px; overflow: hidden; background: var(--white); }
  .slide { position: relative; width: 1200px; height: 675px; overflow: hidden; background: var(--white); font-family: "Carlito", "Calibri", sans-serif; }

  .top-band { position: absolute; left: 0; top: 0; width: 1200px; height: 302px; background: linear-gradient(180deg, var(--band-top), var(--band-bottom)); }
  .slide-title { position: absolute; left: 52px; top: 10px; font-size: 54px; line-height: 60px; font-weight: 700; color: var(--title-blue); letter-spacing: -0.5px; }
  .title-rule { position: absolute; left: 31px; top: 74px; width: 1144px; height: 3px; background: var(--rule); }
  .brand { position: absolute; right: 32px; top: 24px; display: flex; align-items: center; gap: 8px; font-size: 18px; font-weight: 700; color: var(--title-blue); }
  .brand-dot { width: 14px; height: 14px; border-radius: 50%; background: var(--title-blue); }

  .headline { position: absolute; left: 0; top: 176px; width: 1200px; text-align: center; font-size: 42px; font-weight: 700; line-height: 56px; color: var(--gold); }

  .flow { position: absolute; left: 75px; top: 326px; width: 1050px; display: grid; grid-template-columns: 300px 75px 300px 75px 300px; align-items: start; }
  .step-head { height: 58px; display: flex; align-items: center; justify-content: center; color: var(--white); font-size: 36px; line-height: 1; border-radius: 3px; box-shadow: 0 2px 4px rgba(40, 70, 120, 0.18); }
  .step-challenge .step-head { background: var(--step-1); }
  .step-need .step-head { background: var(--step-2); }
  .step-result .step-head { background: var(--step-3); }
  .step-text { margin-top: 14px; padding-left: 2px; font-family: "PT Sans", "Tahoma", sans-serif; font-size: 17px; line-height: 25px; color: var(--ink); }
  .flow-arrow { width: 52px; height: 46px; margin: 6px auto 0; display: block; }

  .footer-band { position: absolute; left: 0; top: 656px; width: 1200px; height: 19px; background: var(--footer); }
  .footer-tab { position: absolute; left: 46px; top: 633px; width: 158px; height: 60px; }
  .footer-mark { position: absolute; left: 78px; top: 642px; display: flex; align-items: center; gap: 8px; font-size: 26px; line-height: 30px; font-weight: 700; color: var(--step-1); }
  .footer-mark .dot { width: 18px; height: 18px; border-radius: 50%; background: var(--step-1); }
</style>
</head>
<body>
<div class="slide">
  <div class="top-band"></div>
  <h1 class="slide-title">IDEA to REALITY</h1>
  <div class="title-rule"></div>
  <div class="brand"><span class="brand-dot"></span>Ridgeline Systems</div>

  <h2 class="headline">A Web-Based Environment for<br>Architecture Decision Analytics</h2>

  <div class="flow">
    <section class="step step-challenge">
      <div class="step-head">The Challenge</div>
      <p class="step-text">Identifying / integrating an organization’s “sources of record” information and making it readily available (assets, budget, systems, references).</p>
    </section>
    <svg class="flow-arrow" viewBox="0 0 52 46" aria-hidden="true">
      <polygon points="0,12 28,12 28,0 52,23 28,46 28,34 0,34" fill="var(--arrow)"/>
    </svg>
    <section class="step step-need">
      <div class="step-head">The Need</div>
      <p class="step-text">A portal solution enabling the rapid ingestion, organization, integration, display and analysis of data from multiple sources.</p>
    </section>
    <svg class="flow-arrow" viewBox="0 0 52 46" aria-hidden="true">
      <polygon points="0,12 28,12 28,0 52,23 28,46 28,34 0,34" fill="var(--arrow)"/>
    </svg>
    <section class="step step-result">
      <div class="step-head">The Result</div>
      <p class="step-text">A collaborative architecture decision support tool that allows users to associate mission guidance with mission execution.</p>
    </section>
  </div>

  <div class="footer-band"></div>
  <svg class="footer-tab" viewBox="0 0 158 60" aria-hidden="true">
    <ellipse cx="79" cy="36" rx="79" ry="30" fill="var(--white)"/>
  </svg>
  <div class="footer-mark"><span class="dot"></span>Q827</div>
</div>
</body>
</html>
```